Book cover for ebook and Physical book for Mind Clutter Collective

I run a non-profit Mind Clutter Collective and I have a new book that needs a cover. For the physical book, I will need a full wrap. The mission is to help individuals Escape the cycle of restless inner chatter. This book is title is "Escape the cycle of restless inner chatter", and subtitle "Release Your Mind from Clutter." I am open to anything design wise, nothing is set in stone. Oh, MCC is pending Trademark.

Target Market(s)

Typically it's Mom's from 25-40

Industry/Entity Type

Mental Health

Font styles to use
Serif

Colors
f37122
9bcb3b
fbed22
0255a3
e34197

Requirements
Must have
• I do like simplicity, yet vibrant colors.
Nice to have
• The authors are Neil R. Dawkins, and Vera Holmquist. For some inspiration individuals refer to me as the Wonder Healer having reversed five incurable diseases.
Should not have
• The cover shouldn't be too busy.

```html
<!DOCTYPE html>
<html lang="en">
<head>
<meta charset="utf-8">
<title>Escape — Book Cover</title>
<link rel="stylesheet" href="https://fonts.googleapis.com/css2?family=EB+Garamond:wght@400;500&display=swap">
<style>
  :root {
    --lime: #9bcb3b;
    --magenta: #e34197;
    --orange: #f37122;
    --yellow: #fbed22;
    --blue: #0255a3;
    --serif: "EB Garamond", Garamond, "Times New Roman", serif;
  }
  html, body {
    margin: 0;
    padding: 0;
    overflow: hidden;
    background: var(--lime);
  }
  .cover {
    position: relative;
    width: 850px;
    height: 1200px;
    overflow: hidden;
    background: var(--lime);
    font-family: var(--serif);
  }
  .band {
    position: absolute;
    left: 0;
    width: 850px;
  }
  .band--top { top: 82px; height: 220px; background: var(--magenta); }
  .band--middle { top: 309px; height: 221px; background: var(--orange); }
  .band--lower { top: 538px; height: 222px; background: var(--magenta); }
  .band--authors { top: 1034px; height: 110px; background: var(--blue); }

  .title-part {
    position: absolute;
    margin: 0;
    color: var(--yellow);
    font-weight: 400;
    font-size: 236px;
    line-height: 1;
    letter-spacing: -6px;
  }
  .title-part--first { left: 6px; top: 62px; }
  .title-part--second { left: 360px; top: 289px; }
  .title-part--third { right: 10px; top: 519px; }

  .subtitle {
    position: absolute;
    right: 88px;
    top: 104px;
    margin: 0;
    color: var(--yellow);
    font-size: 29px;
    line-height: 34px;
    text-align: right;
    text-transform: uppercase;
    font-weight: 400;
  }
  .tagline {
    position: absolute;
    left: 38px;
    top: 828px;
    margin: 0;
    color: var(--blue);
    font-size: 41px;
    line-height: 46px;
    text-transform: uppercase;
    font-weight: 400;
  }
  .authors {
    position: absolute;
    left: 0;
    width: 850px;
    top: 1064px;
    margin: 0;
    color: var(--orange);
    font-size: 38px;
    line-height: 1;
    text-align: center;
    text-transform: uppercase;
    font-weight: 400;
    letter-spacing: 0.5px;
  }
</style>
</head>
<body>
  <div class="cover">
    <div class="band band--top"></div>
    <div class="band band--middle"></div>
    <div class="band band--lower"></div>
    <div class="band band--authors"></div>

    <h1 class="title" aria-label="Escape">
      <span class="title-part title-part--first" aria-hidden="true">ES</span>
      <span class="title-part title-part--second" aria-hidden="true">C</span>
      <span class="title-part title-part--third" aria-hidden="true">APE</span>
    </h1>

    <p class="subtitle">The cycle<br>of<br>restless<br>inner<br>chatter</p>

    <p class="tagline">Release your<br>mind from<br>clutter</p>

    <p class="authors">Neil R. Dawkins &amp; Vera Holmquist</p>
  </div>
</body>
</html>
```